依頼詳細
バイクで周辺のニュータウンに配布を考えています。
量販店よりもかなり安いので、安いとわかるようなチラシに仕上げたいです。
また、片面にウォーターサーバーのサブスクの内容を入れてます。
デザインは近いものでイラストを考えています。
記載項目
社名・電話番号・料金プラン
エアコンの取付・取外しをお得にできます。
エアコン基本設置4m 11,000円~
エアコン基本外し 4,000円(2台台以上)
(外し単品は6,000円)
価格は税込み
サイズ
A5
ページ数
片面
希望イメージ
シンプル 複雑
単色 カラフル
暗い 明るい
日常 高級
遊び心 厳粛
未来的 伝統的
女性的 男性的
希望する色
黄・オレンジ系
納品ファイル
• イラストレーター形式 (.ai)
補足説明
■ 選んだ理由

こちらで想定していたのと全然違う構成に感銘を受けました。
かなり手直しが必要ですが、こちらの路線でチラシを作成しようと思います。

■ 提案者全員のお礼・コメント

今回はたくさんのご応募をいただき大変感謝しております。
たくさんのパターンがあり感動しています。
また、同じような応募をしますのでその際はよろしくお願いいたします

```html
<!DOCTYPE html>
<html lang="ja">
<head>
<meta charset="UTF-8">
<title>エアコン取付・取外し チラシ</title>
<link href="https://fonts.googleapis.com/css2?family=M+PLUS+Rounded+1c:wght@500;800;900&family=Noto+Sans+JP:wght@400;700;900&display=swap" rel="stylesheet">
<style>
  :root{
    --orange:#f28a1c;
    --orange-deep:#e8661a;
    --yellow:#ffd24a;
    --red:#e0301e;
    --ink:#222;
    --grey:#666;
    --sky:#d7ecfa;
    --sky-deep:#a8d2f2;
    --white:#fff;
  }
  *{margin:0;padding:0;box-sizing:border-box}
  html,body{width:857px;height:1200px;overflow:hidden;background:var(--white)}
  .flyer{
    position:relative;width:857px;height:1200px;overflow:hidden;
    font-family:"Noto Sans JP",sans-serif;color:var(--ink);
    background:linear-gradient(180deg,#f4f4f4 0%,#fafafa 28%,#fff3c9 40%,var(--yellow) 58%,var(--orange) 82%,var(--orange-deep) 100%);
  }
  .aircon-visual{
    position:absolute;left:290px;top:20px;width:560px;height:300px;
    background:linear-gradient(180deg,#ffffff 0%,#eef3f7 45%,rgba(120,190,245,.55) 100%);
    border-radius:10px;
  }
  .catch{position:absolute;left:40px;top:28px;width:240px;text-align:center}
  .catch-lead{font-size:22px;line-height:1.4;color:var(--grey);font-weight:700}
  .catch-main{
    margin-top:10px;font-family:"M PLUS Rounded 1c",sans-serif;font-weight:900;
    font-size:40px;line-height:1.3;color:var(--red);
  }
  .catch-main .dot{display:block;font-size:26px;line-height:.8}
  .title{
    position:absolute;left:0;right:0;top:330px;text-align:center;
    font-family:"M PLUS Rounded 1c",sans-serif;font-weight:900;font-size:150px;
    letter-spacing:6px;color:var(--orange-deep);
    -webkit-text-stroke:4px var(--white);paint-order:stroke fill;
    text-shadow:0 0 0 var(--white),0 4px 0 rgba(255,255,255,.9);
  }
  .couple-visual{
    position:absolute;left:115px;top:490px;width:180px;height:150px;
    background:radial-gradient(ellipse at center,#f6d7a8 0%,#e9b47a 70%,rgba(233,180,122,0) 100%);
    border-radius:50%;
  }
  .service-tag{
    position:absolute;left:500px;top:500px;width:320px;height:72px;
    border:3px solid var(--white);display:flex;align-items:center;justify-content:center;
    font-family:"M PLUS Rounded 1c",sans-serif;font-weight:800;font-size:46px;
    color:var(--white);letter-spacing:4px;background:rgba(255,255,255,.08);
  }
  .intro{
    position:absolute;left:50px;top:650px;font-size:27px;font-weight:700;line-height:1.55;
  }
  .price-card{
    position:absolute;top:750px;height:235px;
    border:4px solid var(--white);
    background:radial-gradient(circle at 50% 45%,var(--white) 0%,var(--sky) 45%,var(--sky-deep) 100%);
    padding:18px 24px;
  }
  .price-card.install{left:43px;width:388px}
  .price-card.remove{left:457px;width:372px}
  .price-name{font-family:"M PLUS Rounded 1c",sans-serif;font-weight:800;font-size:38px;line-height:1.3}
  .price{margin-top:14px;font-family:"M PLUS Rounded 1c",sans-serif;font-weight:900;color:var(--red);font-size:72px;line-height:1}
  .price small{font-size:30px}
  .price .tax{font-size:14px;vertical-align:middle;display:inline-block;line-height:1.1}
  .price-note{margin-top:8px;font-size:15px;color:var(--ink)}
  .footer{position:absolute;left:30px;right:30px;top:1015px;height:160px;display:flex;gap:20px;align-items:center}
  .consult{display:flex;align-items:center;gap:14px;width:260px}
  .staff-visual{width:80px;height:100px;border-radius:12px;background:linear-gradient(180deg,#ffe4c2,#f4a860)}
  .consult-text{background:var(--white);border-radius:16px;padding:12px 14px;font-size:22px;font-weight:700;line-height:1.4;color:var(--grey)}
  .company{
    flex:1;background:var(--white);height:140px;padding:16px 26px;
    display:flex;flex-direction:column;justify-content:center;
  }
  .company-name{font-size:30px;font-weight:700}
  .company-tel{display:flex;align-items:center;gap:10px;font-size:50px;font-weight:900;letter-spacing:1px;line-height:1.2}
  .company-tel svg{width:40px;height:40px;flex:none}
</style>
</head>
<body>
<div class="flyer">
  <div class="aircon-visual" role="img" aria-label="壁掛けエアコンから涼しい風が吹き出すイラスト"></div>

  <div class="catch">
    <p class="catch-lead">経験豊富な<br>施工のプロによる</p>
    <p class="catch-main">安心工事<span class="dot">・</span>お得価格</p>
  </div>

  <h1 class="title">エアコン</h1>

  <div class="couple-visual" role="img" aria-label="笑顔の年配夫婦のイラスト"></div>
  <div class="service-tag">取付 取外し</div>

  <p class="intro">大切なお客様のエアコン取付を<br>丁寧にしっかりと施工させていただきます。</p>

  <section class="price-card install">
    <p class="price-name">エアコン<br>基本設置 4m</p>
    <p class="price">11,000<small>円</small><span class="tax">税込</span><small>～</small></p>
  </section>

  <section class="price-card remove">
    <p class="price-name">エアコン<br>基本外し</p>
    <p class="price">4,000<small>円</small><span class="tax">税込</span></p>
    <p class="price-note">（2台以上、外し単品は6,000円）</p>
  </section>

  <footer class="footer">
    <div class="consult">
      <div class="staff-visual" role="img" aria-label="作業員のイラスト"></div>
      <p class="consult-text">お気軽に<br>ご相談ください。</p>
    </div>
    <div class="company">
      <p class="company-name">株式会社 ミライエ</p>
      <p class="company-tel">
        <svg viewBox="0 0 24 24" aria-hidden="true"><path fill="#222" d="M6.6 10.8a15.1 15.1 0 0 0 6.6 6.6l2.2-2.2a1 1 0 0 1 1-.25 11.4 11.4 0 0 0 3.6.57 1 1 0 0 1 1 1V20a1 1 0 0 1-1 1A17 17 0 0 1 3 4a1 1 0 0 1 1-1h3.5a1 1 0 0 1 1 1c0 1.25.2 2.45.57 3.57a1 1 0 0 1-.25 1z"/></svg>
        0120-318-765
      </p>
    </div>
  </footer>
</div>
</body>
</html>
```